hotel's Website

Hotels website redesign for reference pictures, logo etc see http://restwellmarlow.co.uk/

1. 2-3 Special offers on the main page.
2. Booking calender
3. Location Map
4. Picture gallery.
5. Journeyscope reviews.
6. short description
7. Social Media sharing.
8 Phone number and address.

Industry/Entity Type

Hotel

Requirements
Must have
• 1. 2-3 Special offers on the main page.
2. Booking calender
3. Location Map
4. Picture gallery.
5. Journeyscope reviews.
6. short description
7. Social Media sharing.

```html
<!DOCTYPE html>
<html lang="en">
<head>
<meta charset="utf-8">
<title>Restwell Inn Marlow Riverside</title>
<link rel="stylesheet" href="https://fonts.googleapis.com/css2?family=Arimo:wght@400;700&display=swap">
<style>
  :root {
    --page-bg: #d4d4d4;
    --brand-yellow: #f4e35c;
    --brand-square: #2b4f9e;
    --brand-text: #555555;
    --band-dark: #595959;
    --tab-mid: #939393;
    --panel: #949494;
    --nav-light: #ffffff;
    --nav-text: #111111;
    --text-light: #f3f3f3;
    --accent-yellow: #f2df55;
    --divider: #6e6e6e;
    --map-green: #b9c4a8;
    --map-water: #9fb7c9;
  }
  * { box-sizing: border-box; margin: 0; padding: 0; }
  html, body {
    width: 1200px; height: 675px; overflow: hidden;
    background: var(--page-bg);
    font-family: "Arimo", Arial, sans-serif;
  }
  .site { position: relative; width: 1200px; height: 675px; }

  .hero {
    position: absolute; left: 0; top: 0; width: 1200px; height: 286px;
    background: linear-gradient(90deg, #5f6863 0%, #cfccc6 18%, #bdb8b0 40%, #d8d6d1 60%, #b9b5ad 80%, #e3e3e0 100%);
  }
  .hero::after {
    content: ""; position: absolute; inset: 0;
    background: linear-gradient(180deg, rgba(255,255,255,0.15) 0%, rgba(120,115,108,0.25) 100%);
  }

  .gallery {
    position: absolute; left: 783px; top: 232px; display: flex; gap: 8px; z-index: 1;
  }
  .gallery-thumb {
    width: 54px; height: 40px; border: 2px solid #fff;
    box-shadow: 0 1px 3px rgba(0,0,0,0.35);
  }
  .gallery-thumb.t1 { background: linear-gradient(135deg, #c9c3b8, #8e887e); }
  .gallery-thumb.t2 { background: linear-gradient(135deg, #a9b6c0, #6d7d88); }
  .gallery-thumb.t3 { background: linear-gradient(135deg, #d8cdb8, #a69678); }
  .gallery-thumb.t4 { background: linear-gradient(135deg, #b5c1a4, #7b8a6c); }

  .brand {
    position: absolute; left: 163px; top: 0; width: 220px; height: 111px;
    background: var(--brand-yellow);
    box-shadow: 1px 2px 3px rgba(0,0,0,0.3);
    display: flex; align-items: flex-start;
  }
  .brand-square { width: 84px; height: 97px; margin: 5px 0 0 5px; background: var(--brand-square); }
  .brand-name { margin: 15px 0 0 11px; font-size: 25px; line-height: 31px; color: var(--brand-text); }

  .availability {
    position: absolute; left: 163px; top: 326px; width: 220px; height: 40px;
    background: var(--band-dark); color: var(--accent-yellow);
    font-size: 13.5px; text-align: center; line-height: 40px;
  }

  .calendar {
    position: absolute; left: 403px; top: 298px; width: 180px; height: 96px;
    background: #fff; padding: 4px 8px; color: #333;
  }
  .calendar-title { font-size: 10px; font-weight: 700; text-align: center; line-height: 12px; margin-bottom: 1px; }
  .calendar table { width: 100%; border-collapse: collapse; font-size: 8.5px; text-align: center; }
  .calendar th { color: #777; font-weight: 400; height: 11px; }
  .calendar td { height: 11px; }
  .calendar td.is-booked { background: var(--accent-yellow); }

  .offers { position: absolute; left: 601px; top: 298px; display: flex; gap: 8px; }
  .offer {
    width: 92px; height: 96px; background: var(--band-dark); color: #fff;
    padding: 9px 8px; font-size: 10.5px; line-height: 13px;
  }
  .offer-label { color: var(--accent-yellow); font-size: 9px; letter-spacing: 0.5px; margin-bottom: 4px; }
  .offer-title { font-weight: 700; margin-bottom: 6px; }
  .offer-price { font-size: 15px; line-height: 18px; }

  .map {
    position: absolute; left: 903px; top: 298px; width: 120px; height: 96px;
    background: linear-gradient(160deg, var(--map-green) 0%, #cfd6c2 55%, var(--map-water) 100%);
  }
  .map svg { position: absolute; left: 50px; top: 28px; }

  .nav-band {
    position: absolute; left: 0; top: 403px; width: 1200px; height: 40px;
    background: var(--band-dark);
  }
  .nav { position: absolute; left: 163px; top: 0; height: 40px; display: flex; list-style: none; }
  .nav-welcome {
    width: 220px; background: var(--tab-mid); color: #fff;
    font-size: 21px; padding: 14px 0 0 43px; line-height: 24px;
  }
  .nav-item {
    width: 160px; height: 40px; text-align: center;
    font-size: 11.3px; line-height: 42px;
    background: var(--nav-light); color: var(--nav-text);
    border-left: 1px solid #9a9a9a;
  }
  .nav-item.is-active { background: var(--band-dark); color: #fff; border-left: none; }

  .content {
    position: absolute; left: 163px; top: 448px; width: 860px; height: 227px;
    background: var(--panel);
  }
  .intro {
    position: absolute; left: 43px; top: 30px; width: 522px;
    font-size: 12.3px; line-height: 17.1px; color: var(--text-light);
  }
  .review {
    position: absolute; left: 43px; top: 162px; width: 522px;
    color: var(--text-light); font-size: 12.3px; line-height: 17.1px;
  }
  .review-head { display: flex; align-items: center; gap: 8px; font-weight: 700; }
  .rating { display: flex; gap: 3px; }
  .rating span { width: 9px; height: 9px; border-radius: 50%; background: var(--accent-yellow); }
  .divider {
    position: absolute; left: 605px; top: 31px; width: 1px; height: 158px;
    background: var(--divider);
  }
  .contact {
    position: absolute; left: 658px; top: 31px;
    font-size: 12.8px; line-height: 18.4px; color: var(--text-light); font-style: normal;
  }
  .contact .gap { display: block; height: 10px; }
  .share {
    position: absolute; left: 658px; top: 182px; display: flex; align-items: center; gap: 7px;
    font-size: 12.8px; color: var(--text-light);
  }
  .share-dot { width: 18px; height: 18px; border-radius: 50%; background: var(--band-dark); }
</style>
</head>
<body>
<div class="site">
  <div class="hero" role="img" aria-label="Photograph of a bright twin hotel room with white pillows, striped bedspreads and bedside tables"></div>

  <div class="gallery">
    <div class="gallery-thumb t1" role="img" aria-label="Gallery photo of the hotel lobby"></div>
    <div class="gallery-thumb t2" role="img" aria-label="Gallery photo of a double bedroom"></div>
    <div class="gallery-thumb t3" role="img" aria-label="Gallery photo of the breakfast room"></div>
    <div class="gallery-thumb t4" role="img" aria-label="Gallery photo of the riverside garden"></div>
  </div>

  <header class="brand">
    <div class="brand-square"></div>
    <div class="brand-name">Restwell<br>Marlow</div>
  </header>

  <div class="availability">CHECK AVAILABILITY</div>

  <section class="calendar" aria-label="Booking calendar">
    <div class="calendar-title">June 2025</div>
    <table>
      <tr><th>Mo</th><th>Tu</th><th>We</th><th>Th</th><th>Fr</th><th>Sa</th><th>Su</th></tr>
      <tr><td></td><td></td><td></td><td></td><td></td><td></td><td>1</td></tr>
      <tr><td>2</td><td>3</td><td>4</td><td>5</td><td>6</td><td>7</td><td>8</td></tr>
      <tr><td>9</td><td>10</td><td>11</td><td>12</td><td class="is-booked">13</td><td class="is-booked">14</td><td>15</td></tr>
      <tr><td>16</td><td>17</td><td>18</td><td>19</td><td>20</td><td>21</td><td>22</td></tr>
      <tr><td>23</td><td>24</td><td>25</td><td>26</td><td>27</td><td>28</td><td>29</td></tr>
      <tr><td>30</td><td></td><td></td><td></td><td></td><td></td><td></td></tr>
    </table>
  </section>

  <section class="offers" aria-label="Special offers">
    <div class="offer"><div class="offer-label">OFFER</div><div class="offer-title">Weekend Break</div><div class="offer-price">from £89</div></div>
    <div class="offer"><div class="offer-label">OFFER</div><div class="offer-title">Bed &amp; Breakfast</div><div class="offer-price">from £65</div></div>
    <div class="offer"><div class="offer-label">OFFER</div><div class="offer-title">Stay 3, Pay 2</div><div class="offer-price">save 33%</div></div>
  </section>

  <div class="map" role="img" aria-label="Location map of the hotel by the river in Marlow">
    <svg width="20" height="28" viewBox="0 0 20 28" aria-hidden="true">
      <path d="M10 1 C4.5 1 1 5 1 10 C1 17 10 27 10 27 C10 27 19 17 19 10 C19 5 15.5 1 10 1 Z" fill="#595959"/>
      <circle cx="10" cy="10" r="3.5" fill="#f2df55"/>
    </svg>
  </div>

  <nav class="nav-band">
    <ul class="nav">
      <li class="nav-welcome">welcome</li>
      <li class="nav-item is-active">home</li>
      <li class="nav-item">explore hotel</li>
      <li class="nav-item">apartments</li>
      <li class="nav-item">contact</li>
    </ul>
  </nav>

  <main class="content">
    <p class="intro">I'm a paragraph. Once you supply me with the content you would like to go here I will place it here for you. This will be the text that is located here on the page!I'm a paragraph. Once you supply me with the content you would like to go here I will place it here for you. This will be the text that is located here on the page!I'm a paragraph. Once you supply me with the content you would like to go here I will place it here for you. This will be the text that is located here on the page!I'm a paragraph. Once you supply me with the content you would like to go here I will place it here for you.</p>
    <div class="review">
      <div class="review-head">Journeyscope reviews
        <span class="rating"><span></span><span></span><span></span><span></span><span></span></span>
      </div>
      <p>"Quiet rooms, friendly staff and a lovely walk along the river." – Anna, May 2025</p>
    </div>
    <div class="divider"></div>
    <address class="contact">
      Restwell Inn<br>Marlow Riverside<br>
      <span class="gap"></span>
      SL7 4QZ<br>
      <span class="gap"></span>
      stay@restwellmarlow.co.uk<br>
      <span class="gap"></span>
      Tel:&nbsp; 020-555-0147<br>
      Fax: 020-555-0147
    </address>
    <div class="share">Share
      <span class="share-dot" aria-label="Share on social network one"></span>
      <span class="share-dot" aria-label="Share on social network two"></span>
      <span class="share-dot" aria-label="Share on social network three"></span>
    </div>
  </main>
</div>
</body>
</html>
```